Etiketten für Gin
Zielgruppe
Wir sind eine kleine neue Brennerei im bayerischen Oberland und werden unter den Namen „Silver Kite“ und „Silver Kite Lemon“ zwei GIN-Sorten auf den Markt bringen.
Der GIN wird online und vor Ort verkauft und sollte daher eine exklusiv-auffällige Optik haben um die Kunden zu beeindrucken. Zielkunden sind anspruchsvolle Genießer, welche die bayerische Gastlichkeit und Lebenskultur schätzen.
Neu an den beiden Gins ist, dass sie mit Blütenpollen destilliert werden, was auf dem Etikett erscheinen muss.
Aufgabenstellung
Wir suchen zwei sich ähnelnde GIN-Etiketten deren Design ausdrückt, dass es sich um handgemachte und hochwertige GIN handelt, deren Zutat Blütenpollen bisher einzigartig ist.
Statt der oft üblichen Bezeichnung „London Dry Gin“ soll „Halmberg Dry Gin“ und „handcrafted“ auf dem Etikett erscheinen, zusätzlich natürlich die verkehrsüblichen Angaben.
Abgefüllt wird in weißen 500ml Flaschen Typ Vendu mit Korkverschluss von kapselix.com.
Sinnvoll halten wir ein Frontetikett, lassen aber gerne auch andere Vorschläge zu.

```html
<!DOCTYPE html>
<html lang="de">
<head>
<meta charset="utf-8">
<title>Halmberg Dry Gin – Etiketten</title>
<link rel="stylesheet" href="https://fonts.googleapis.com/css2?family=Open+Sans:wght@300;400;600&family=Oswald:wght@300&family=Mrs+Saint+Delafield&family=Nothing+You+Could+Do&display=swap">
<style>
  :root {
    --canvas-bg: #f3f3f3;
    --label-bg: #ffffff;
    --neck-bg: #e6e6e6;
    --ink: #555555;
    --ink-dark: #4a4a4a;
    --ink-soft: #a9a9a9;
    --rose: #c63f98;
    --rose-band: #c9a4c7;
    --lemon: #f2dc00;
    --lemon-band: #fff200;
  }
  * { box-sizing: border-box; margin: 0; padding: 0; }
  html, body { width: 914px; height: 1200px; overflow: hidden; }
  body {
    background: var(--canvas-bg);
    font-family: "Open Sans", Arial, sans-serif;
    color: var(--ink);
    position: relative;
  }
  .variant {
    position: absolute;
    top: 0;
    width: 376px;
    height: 1200px;
  }
  .variant--rose { left: 50px; --accent: var(--rose); --band: var(--rose-band); }
  .variant--lemon { left: 470px; --accent: var(--lemon); --band: var(--lemon-band); }

  /* neck label */
  .neck-label {
    position: absolute;
    left: 130px;
    top: 277px;
    width: 114px;
    height: 80px;
    background: var(--neck-bg);
    padding: 3px 10px 0;
    text-align: center;
  }
  .neck-label__caption {
    font-family: "Oswald", sans-serif;
    font-weight: 300;
    font-size: 6px;
    line-height: 8px;
    color: #555;
  }
  .neck-label__entry {
    display: block;
    height: 12px;
    margin: 0 0 3px;
    background: var(--band);
    font-family: "Nothing You Could Do", cursive;
    font-size: 10px;
    line-height: 13px;
    color: #222;
  }

  /* front label */
  .front-label {
    position: absolute;
    left: 0;
    top: 640px;
    width: 376px;
    height: 320px;
    background: var(--label-bg);
  }
  .front-label__volume {
    position: absolute;
    left: 12px;
    bottom: 16px;
    transform-origin: left bottom;
    transform: rotate(-90deg) translateY(100%);
    font-weight: 300;
    font-size: 13px;
    letter-spacing: 0.3em;
    color: var(--ink-soft);
    white-space: nowrap;
  }
  .front-label__volume span { margin-left: 16px; }
  .brand {
    position: absolute;
    left: 95px;
    top: 12px;
    font-weight: 600;
    font-size: 15px;
    line-height: 24px;
    letter-spacing: 0.5em;
    color: var(--accent);
  }
  .seed-art {
    position: absolute;
    left: 40px;
    top: 64px;
    width: 300px;
    height: 150px;
  }
  .product-name {
    position: absolute;
    right: 10px;
    top: 228px;
    font-weight: 400;
    font-size: 16px;
    line-height: 20px;
    letter-spacing: 0.28em;
    color: var(--accent);
    white-space: nowrap;
  }
  .variant--lemon .product-name { font-size: 14px; letter-spacing: 0.22em; }
  .handcrafted {
    position: absolute;
    left: 222px;
    top: 250px;
    font-family: "Mrs Saint Delafield", cursive;
    font-size: 30px;
    line-height: 32px;
    color: var(--ink-dark);
  }
  .variant--lemon .handcrafted { left: 184px; }
  .pollen-note {
    position: absolute;
    right: 36px;
    top: 294px;
    font-size: 7px;
    line-height: 10px;
    letter-spacing: 0.16em;
    color: var(--ink);
    white-space: nowrap;
  }
  .variant--lemon .pollen-note { right: 76px; }
</style>
</head>
<body>

<section class="variant variant--rose" aria-label="Silver Kite">
  <div class="neck-label">
    <p class="neck-label__caption">Batch No.</p>
    <span class="neck-label__entry">003/166</span>
    <p class="neck-label__caption">Date of Distillation</p>
    <span class="neck-label__entry">12/2020</span>
    <p class="neck-label__caption">Hand bottled for</p>
    <span class="neck-label__entry">Lena Hartl</span>
  </div>
  <div class="front-label">
    <p class="front-label__volume">500ml<span>Alc.43%vol.</span></p>
    <p class="brand">HALMBERG<br>DRY GIN</p>
    <svg class="seed-art" role="img" aria-label="Illustration: fliegende Pusteblumensamen und eine Figur, die an einem Samen schwebt" viewBox="0 0 300 150">
      <defs>
        <linearGradient id="seed-rose" x1="0" y1="0" x2="1" y2="0">
          <stop offset="0" stop-color="#ffffff"/>
          <stop offset="0.45" stop-color="#f1e6ee"/>
          <stop offset="1" stop-color="#e7b6d3"/>
        </linearGradient>
      </defs>
      <rect width="300" height="150" fill="url(#seed-rose)"/>
    </svg>
    <p class="product-name">SILVER KITE</p>
    <p class="handcrafted">Handcrafted</p>
    <p class="pollen-note">MIT BLÜTENPOLLEN DESTILLIERT</p>
  </div>
</section>

<section class="variant variant--lemon" aria-label="Silver Kite Lemon">
  <div class="neck-label">
    <p class="neck-label__caption">Batch No.</p>
    <span class="neck-label__entry">003/166</span>
    <p class="neck-label__caption">Date of Distillation</p>
    <span class="neck-label__entry">12/2020</span>
    <p class="neck-label__caption">Hand bottled for</p>
    <span class="neck-label__entry">Lena Hartl</span>
  </div>
  <div class="front-label">
    <p class="front-label__volume">500ml<span>Alc.43%vol.</span></p>
    <p class="brand">HALMBERG<br>DRY GIN</p>
    <svg class="seed-art" role="img" aria-label="Illustration: fliegende Pusteblumensamen und eine Figur, die an einem Samen schwebt" viewBox="0 0 300 150">
      <defs>
        <linearGradient id="seed-lemon" x1="0" y1="0" x2="1" y2="0">
          <stop offset="0" stop-color="#ffffff"/>
          <stop offset="0.45" stop-color="#f0ede6"/>
          <stop offset="1" stop-color="#f1e58a"/>
        </linearGradient>
      </defs>
      <rect width="300" height="150" fill="url(#seed-lemon)"/>
    </svg>
    <p class="product-name">SILVER KITE LEMON</p>
    <p class="handcrafted">Handcrafted</p>
    <p class="pollen-note">MIT BLÜTENPOLLEN DESTILLIERT</p>
  </div>
</section>

</body>
</html>
```